Online Home Automation business needs business card design

New business starting up that sells home-automation products in Australia. Business card needs to look very polished and professional. The business name is "Vesk Automation".
Updates

Thank you all for the great designs, We are really impressed. We are in the process of deciding on a design but keep the designs coming in.

Industry/Entity Type

Business

```html
<!DOCTYPE html>
<html lang="en">
<head>
<meta charset="utf-8">
<title>Vesk Automation – Business Card</title>
<link href="https://fonts.googleapis.com/css2?family=Open+Sans:wght@300;400;600;700&display=swap" rel="stylesheet">
<style>
  :root {
    --page-bg: #e9e6e1;
    --card-white: #f2f2f2;
    --card-grey: #d9d9d9;
    --card-dark: #1c1c1c;
    --card-darker: #0e0e0e;
    --accent-red: #e0252b;
    --text-dark: #1a1a1a;
    --text-muted: #8a8a8a;
    --text-light: #f4f4f4;
  }
  * { margin: 0; padding: 0; box-sizing: border-box; }
  html, body {
    width: 1200px; height: 1023px; overflow: hidden;
    background: var(--page-bg);
    font-family: "Open Sans", Arial, sans-serif;
  }
  .stage { position: relative; width: 1200px; height: 1023px; }
  .card {
    position: absolute; top: 356px;
    width: 540px; height: 310px;
    border-radius: 6px; overflow: hidden;
    box-shadow: 0 14px 30px rgba(0,0,0,.25);
  }
  .card--front { left: 40px; background: linear-gradient(135deg, var(--card-white), var(--card-grey)); }
  .card--back  { left: 620px; background: linear-gradient(135deg, #2a2a2a, var(--card-darker)); }

  .front-shape { position: absolute; inset: 0; }

  .illustration-area {
    position: absolute; right: 22px; top: 14px;
    width: 130px; height: 120px; border-radius: 50% 50% 40% 50%;
    background: radial-gradient(circle at 45% 40%, #3a3a3a, #111 75%);
    opacity: .9;
  }

  .brand { position: absolute; left: 28px; top: 38px; display: flex; align-items: center; gap: 14px; }
  .brand__dot {
    width: 56px; height: 56px; border-radius: 50%;
    background: var(--accent-red);
  }
  .brand__name {
    font-weight: 700; font-size: 26px; line-height: 1.05; color: var(--text-dark);
  }

  .person { position: absolute; left: 28px; top: 128px; }
  .person__name { font-weight: 700; font-size: 19px; color: var(--text-dark); }
  .person__role { font-weight: 400; font-size: 12px; color: var(--text-muted); }

  .contacts { position: absolute; left: 28px; bottom: 22px; list-style: none; }
  .contacts li {
    display: flex; align-items: center; gap: 8px;
    font-size: 12.5px; color: var(--text-light); line-height: 19px;
  }
  .contacts svg { width: 12px; height: 12px; flex: none; }

  .address { position: absolute; right: 24px; top: 170px; text-align: right; font-size: 12.5px; line-height: 17px; color: var(--text-light); }
  .address__company { color: var(--accent-red); font-weight: 700; }

  .back-brand {
    position: absolute; left: 40px; top: 50%; transform: translateY(-50%);
    display: flex; align-items: center; gap: 18px;
  }
  .back-brand__dot { width: 78px; height: 78px; border-radius: 50%; background: var(--accent-red); }
  .back-brand__name { font-weight: 700; font-size: 34px; line-height: 1.05; color: var(--text-light); }

  .back-decoration {
    position: absolute; right: -30px; bottom: -30px;
    width: 220px; height: 220px; border-radius: 50%;
    background: radial-gradient(circle, rgba(255,255,255,.06), rgba(255,255,255,0) 70%);
  }
</style>
</head>
<body>
<main class="stage">

  <section class="card card--front">
    <svg class="front-shape" viewBox="0 0 540 310" preserveAspectRatio="none" aria-hidden="true">
      <defs>
        <linearGradient id="darkBand" x1="0" y1="0" x2="1" y2="1">
          <stop offset="0" stop-color="#262626"/>
          <stop offset="1" stop-color="#0e0e0e"/>
        </linearGradient>
      </defs>
      <path d="M0,222 L250,222 C330,222 360,180 392,118 C420,62 462,26 540,22 L540,310 L0,310 Z" fill="url(#darkBand)"/>
      <path d="M0,222 L250,222 C330,222 360,180 392,118 C420,62 462,26 540,22" fill="none" stroke="var(--accent-red)" stroke-width="4"/>
    </svg>

    <div class="illustration-area" role="img" aria-label="Illustration of a bird head in black, white and red"></div>

    <div class="brand">
      <span class="brand__dot"></span>
      <span class="brand__name">Vesk<br>Automation</span>
    </div>

    <div class="person">
      <p class="person__name">Mira Castell</p>
      <p class="person__role">Director</p>
    </div>

    <ul class="contacts">
      <li>
        <svg viewBox="0 0 12 12"><rect width="12" height="12" rx="2" fill="var(--accent-red)"/><path d="M4 3l1.2 1.6-.7.8c.5.9 1.1 1.5 2 2l.8-.7L9 8l-.6 1C6 8.8 3.4 6.3 3 3.6z" fill="#fff"/></svg>
        (07) 5550 1234
      </li>
      <li>
        <svg viewBox="0 0 12 12"><rect width="12" height="12" rx="2" fill="var(--accent-red)"/><rect x="2.5" y="3.5" width="7" height="5" fill="none" stroke="#fff" stroke-width="1"/><path d="M2.5 3.5L6 6.5 9.5 3.5" fill="none" stroke="#fff" stroke-width="1"/></svg>
        info@veskautomation.com.au
      </li>
      <li>
        <svg viewBox="0 0 12 12"><rect width="12" height="12" rx="2" fill="var(--accent-red)"/><circle cx="6" cy="6" r="3.5" fill="none" stroke="#fff" stroke-width="1"/><path d="M2.5 6h7M6 2.5c-1.5 2-1.5 5 0 7M6 2.5c1.5 2 1.5 5 0 7" fill="none" stroke="#fff" stroke-width=".8"/></svg>
        www.veskautomation.com.au
      </li>
    </ul>

    <address class="address">
      <span class="address__company">Vesk Automation</span><br>
      Unit 7, 12 Harlow Street,<br>
      Brookvale Qld 4100
    </address>
  </section>

  <section class="card card--back">
    <div class="back-decoration" role="img" aria-label="Faint large bird head decoration"></div>
    <div class="back-brand">
      <span class="back-brand__dot"></span>
      <span class="back-brand__name">Vesk<br>Automation</span>
    </div>
  </section>

</main>
</body>
</html>
```